Solace Chiropractic & Acupuncture Business Cards

I need a business card design that feels elevated. I am open to any of the logo designs uploaded. We have two doctors so I'll need to be able to change out the names.

Information:
Marnie Toller D.C., L.Ac., Dipl. OM
584 W 12th St, Ste 320
Larkfield, NE 67419
solacegrove.net
402-555-0147
drmarnie@solacegrove.com
Updates

We have designs we like now, we are just trying to choose between top contenders. Thanks for your submissions!

Contact Information for Business Card

noted in description

Requirements
Must have
• ability to edit info if possible
Nice to have
• Please see our website solacegrove.net for our style and colors

```html
<!DOCTYPE html>
<html lang="en">
<head>
<meta charset="utf-8">
<title>Solace Chiropractic &amp; Acupuncture – Business Cards</title>
<link href="https://fonts.googleapis.com/css2?family=Playfair+Display:wght@400&family=Roboto:wght@300;400&display=swap" rel="stylesheet">
<style>
  :root {
    --backdrop: #262626;
    --slate: #41445a;
    --sand: #d8d0c3;
    --paper: #f3f2ef;
    --ink: #3d4054;
    --muted: #5e616e;
    --icon: #b9b3a8;
    --card-w: 484px;
    --card-h: 293px;
  }
  * { margin: 0; padding: 0; box-sizing: border-box; }
  html, body { width: 1200px; height: 576px; overflow: hidden; }
  body { background: var(--backdrop); position: relative; }

  .card {
    position: absolute;
    top: 138px;
    width: var(--card-w);
    height: var(--card-h);
    border-radius: 10px;
    overflow: hidden;
  }

  /* Front */
  .card-front { left: 102px; background: var(--slate); }
  .front-brand {
    position: absolute;
    right: 28px;
    top: 142px;
    text-align: right;
    font-family: "Playfair Display", serif;
    font-weight: 400;
    color: var(--sand);
  }
  .front-brand .brand-name { display: block; font-size: 70px; line-height: 1; }
  .front-brand .brand-tagline {
    display: block;
    font-size: 11px;
    letter-spacing: 0.5px;
    text-transform: uppercase;
    margin-top: 6px;
  }
  .front-url {
    position: absolute;
    right: 26px;
    bottom: 20px;
    font-family: "Roboto", sans-serif;
    font-weight: 400;
    font-size: 13px;
    letter-spacing: 2.6px;
    color: #ecebe8;
  }

  /* Back */
  .card-back { left: 596px; background: var(--paper); }
  .back-shape { position: absolute; inset: 0; }
  .back-brand {
    position: absolute;
    left: 0;
    width: 228px;
    top: 108px;
    text-align: center;
    font-family: "Playfair Display", serif;
    font-weight: 400;
    color: var(--sand);
  }
  .back-brand .brand-name { display: block; font-size: 32px; line-height: 1; letter-spacing: 1px; }
  .back-brand .brand-tagline {
    display: block;
    font-size: 12px;
    line-height: 1.35;
    text-transform: uppercase;
    margin-top: 64px;
  }

  .contact {
    position: absolute;
    left: 278px;
    top: 70px;
    font-family: "Roboto", sans-serif;
    font-weight: 300;
    color: var(--muted);
  }
  .contact-name {
    font-family: "Playfair Display", serif;
    font-weight: 400;
    font-size: 21px;
    color: var(--ink);
    line-height: 1.1;
  }
  .contact-credentials { font-size: 12px; margin-top: 2px; }
  .contact-address { font-size: 12px; line-height: 17.5px; margin-top: 22px; }
  .contact-list { list-style: none; font-size: 12px; line-height: 17.5px; }
  .contact-list li { display: flex; align-items: center; gap: 9px; }
  .contact-list svg { width: 9px; height: 9px; flex: none; }
</style>
</head>
<body>

  <section class="card card-front" aria-label="Card front">
    <div class="front-brand">
      <span class="brand-name">Solace</span>
      <span class="brand-tagline">Chiropractic &amp; Acupuncture</span>
    </div>
    <div class="front-url">www.solacegrove.net</div>
  </section>

  <section class="card card-back" aria-label="Card back">
    <svg class="back-shape" viewBox="0 0 484 293" preserveAspectRatio="none" aria-hidden="true">
      <path d="M0 0 H196 Q282 146 190 293 H0 Z" fill="var(--sand)" transform="translate(8 0)"/>
      <path d="M0 0 H190 Q276 146 184 293 H0 Z" fill="var(--slate)"/>
    </svg>

    <div class="back-brand">
      <span class="brand-name">SOLACE</span>
      <span class="brand-tagline">Chiropractic<br>&amp; Acupuncture</span>
    </div>

    <div class="contact">
      <div class="contact-name">Dr. Marnie Toller</div>
      <div class="contact-credentials">D.C., L.Ac., Dipl. OM</div>
      <div class="contact-address">584 W 12th St, Ste 320<br>Larkfield, NE 67419</div>
      <ul class="contact-list">
        <li>
          <svg viewBox="0 0 10 10"><path d="M2 0.5 L3.6 2.6 L2.7 3.7 Q3.8 5.9 6.3 7.3 L7.4 6.4 L9.5 8 L8.4 9.5 Q3.5 9 0.5 1.6 Z" fill="var(--icon)"/></svg>
          402-555-0147
        </li>
        <li>
          <svg viewBox="0 0 10 10"><circle cx="5" cy="5" r="4" fill="none" stroke="var(--icon)" stroke-width="1.2"/><circle cx="5" cy="5" r="1.6" fill="none" stroke="var(--icon)" stroke-width="1.1"/></svg>
          drmarnie@solacegrove.com
        </li>
        <li>
          <svg viewBox="0 0 10 10"><circle cx="5" cy="5" r="4.2" fill="none" stroke="var(--icon)" stroke-width="1"/><path d="M0.8 5 H9.2 M5 0.8 Q2.6 5 5 9.2 M5 0.8 Q7.4 5 5 9.2" fill="none" stroke="var(--icon)" stroke-width="0.8"/></svg>
          www.solacegrove.net
        </li>
      </ul>
    </div>
  </section>

</body>
</html>
```